Design Invitation using a mobile phone screen image

This invitation is for 12 year olds finishing primary school so make it fun and bright.
Invitation should be an kavrel with a text message saying.....
Dress in your best (insert emoticons - boy in long pants/girl in dress) for your Year 6 farewell dinner (insert emoticon with tear) on Monday 12 December at 6 pm (insert emoticons - party hat, thumbs up and bowl of icecream). Going 2b a gr8 night!
rsvp YES PLEASE and your name to 0459XXXXXXX

Target Market(s)

12/13 years old boys and girls

Industry/Entity Type

School

Requirements
Must have
• Must be bright and look like a text message - it can have an artwork within it as if the invite has been texted and then a comment is made after the image.
• Must us an kavrel screen as the invitation but so we dont have to cut it out it can be a rectanglar card

```html
<!DOCTYPE html>
<html lang="en">
<head>
<meta charset="utf-8">
<title>Year 6 Farewell Dinner Invitation</title>
<link href="https://fonts.googleapis.com/css2?family=Arimo:wght@400;700&display=swap" rel="stylesheet">
<style>
  :root {
    --navy: #1b1e4b;
    --lime: #8dbf2e;
    --yellow-green: #cfdc1f;
    --phone-body: #141414;
    --phone-rim: #8a8a8e;
    --screen-white: #ffffff;
    --bar-grey: #f7f7f8;
    --ios-blue: #2d6fd0;
    --bubble-grey: #e9e9eb;
    --text-dark: #3a3a3a;
    --kb-bg: #d1d5db;
    --key-white: #ffffff;
    --key-dark: #abb0ba;
    --key-shadow: #888c94;
  }
  * { box-sizing: border-box; margin: 0; padding: 0; }
  html, body { width: 933px; height: 1200px; overflow: hidden; }
  body { font-family: "Arimo", Helvetica, Arial, sans-serif; position: relative; }

  .backdrop {
    position: absolute; inset: 0;
    background: linear-gradient(160deg, var(--lime) 0%, var(--navy) 35%, var(--yellow-green) 55%, var(--navy) 75%, var(--lime) 100%);
  }

  .phone {
    position: absolute; left: 197px; top: 49px; width: 543px; height: 1103px;
    background: var(--phone-body); border-radius: 82px;
    border: 4px solid var(--phone-rim);
  }
  .side-button { position: absolute; background: var(--phone-rim); width: 4px; border-radius: 2px; }
  .earpiece-camera { position: absolute; left: 390px; top: 111px; width: 11px; height: 11px; border-radius: 50%; background: #2c3a55; border: 2px solid #333; }
  .earpiece { position: absolute; left: 433px; top: 113px; width: 74px; height: 5px; border-radius: 3px; background: #4a4a4a; }
  .home-button { position: absolute; left: 433px; top: 1048px; width: 72px; height: 72px; border-radius: 50%; border: 3px solid #333; }

  .screen { position: absolute; left: 230px; top: 177px; width: 477px; height: 849px; background: var(--screen-white); overflow: hidden; }

  .status-bar { position: absolute; left: 0; top: 0; width: 100%; height: 20px; font-size: 12px; color: #111; display: flex; align-items: center; justify-content: space-between; padding: 0 5px; }
  .status-bar .time { font-weight: 700; position: absolute; left: 0; right: 0; text-align: center; }
  .battery { display: inline-block; width: 26px; height: 9px; background: #111; border-radius: 2px; vertical-align: middle; margin-left: 3px; }

  .nav-bar { position: absolute; top: 20px; width: 100%; height: 70px; background: var(--bar-grey); border-bottom: 1px solid #dcdcdc; display: flex; align-items: center; font-size: 22px; }
  .nav-back { position: absolute; left: 24px; color: var(--ios-blue); display: flex; align-items: center; gap: 6px; }
  .nav-title { position: absolute; left: 0; right: 0; text-align: center; font-weight: 700; color: #333; }
  .nav-details { position: absolute; right: 26px; color: var(--ios-blue); }

  .message-bubble {
    position: absolute; left: 40px; top: 128px; width: 343px; height: 200px;
    background: var(--bubble-grey); border-radius: 24px;
    padding: 20px 10px 0 21px; font-size: 21px; line-height: 26.7px; color: var(--text-dark);
  }
  .message-bubble strong { font-weight: 700; white-space: nowrap; }
  .bubble-tail { position: absolute; left: 33px; top: 306px; }

  .compose-bar { position: absolute; top: 478px; width: 100%; height: 50px; background: var(--bar-grey); border-top: 1px solid #e2e2e2; }
  .compose-field { position: absolute; left: 61px; top: 9px; width: 398px; height: 33px; border: 1px solid #cfcfcf; border-radius: 6px; background: #fff; font-size: 20px; color: #b9b9b9; padding: 4px 8px; }
  .compose-field::before { content: ""; position: absolute; left: 7px; top: 5px; width: 2px; height: 22px; background: var(--ios-blue); }
  .icon-camera { position: absolute; left: 15px; top: 12px; }
  .icon-mic-round { position: absolute; left: 431px; top: 8px; }

  .keyboard { position: absolute; top: 528px; width: 100%; height: 321px; background: var(--kb-bg); padding-top: 17px; }
  .key-row { display: flex; justify-content: center; gap: 9px; height: 57px; margin-bottom: 23px; }
  .key {
    width: 39px; height: 57px; background: var(--key-white); border-radius: 6px;
    box-shadow: 0 2px 0 var(--key-shadow); display: flex; align-items: center; justify-content: center;
    font-size: 32px; color: #111;
  }
  .key.dark { background: var(--key-dark); }
  .row-two { padding: 0; }
  .row-three .key.shift { width: 54px; margin-right: 20px; }
  .row-three .key.delete { width: 54px; margin-left: 20px; }
  .row-bottom { justify-content: flex-start; padding-left: 5px; }
  .row-bottom .key { font-size: 24px; }
  .key.numbers { width: 50px; }
  .key.globe { width: 50px; }
  .key.dictate { width: 39px; }
  .key.space { width: 182px; }
  .key.search { width: 109px; color: #888; background: var(--key-dark); }
</style>
</head>
<body>
  <div class="backdrop" role="img" aria-label="Bright zigzag chevron pattern in navy, lime and yellow-green"></div>

  <div class="phone"></div>
  <span class="side-button" style="left:193px;top:180px;height:40px"></span>
  <span class="side-button" style="left:193px;top:262px;height:70px"></span>
  <span class="side-button" style="left:193px;top:350px;height:70px"></span>
  <span class="side-button" style="left:740px;top:262px;height:70px"></span>
  <span class="earpiece-camera"></span>
  <span class="earpiece"></span>
  <span class="home-button"></span>

  <main class="screen">
    <div class="status-bar">
      <span>●●●●● 〜</span>
      <span class="time">9:41 AM</span>
      <span>✱ 100%<span class="battery"></span></span>
    </div>

    <header class="nav-bar">
      <span class="nav-back">
        <svg width="14" height="24" viewBox="0 0 14 24"><path d="M12 2 L3 12 L12 22" fill="none" stroke="#2d6fd0" stroke-width="3" stroke-linecap="round" stroke-linejoin="round"/></svg>
        Messages
      </span>
      <span class="nav-title">PARTY!</span>
      <span class="nav-details">Details</span>
    </header>

    <svg class="bubble-tail" width="20" height="24" viewBox="0 0 20 24"><path d="M20 0 L20 22 Q8 24 0 22 Q10 16 8 0 Z" fill="#e9e9eb"/></svg>
    <p class="message-bubble">Dress in your best 🚶‍♂️💃 for your Year 6 farewell dinner 😢 on <strong>Monday 12 December at 6pm</strong> 🎉👍🍧 Going 2b a gr8 night! rsvp YES PLEASE and your name to 0459XXXXXXX.</p>

    <div class="compose-bar">
      <svg class="icon-camera" width="32" height="24" viewBox="0 0 32 24"><rect x="1" y="5" width="30" height="18" rx="3" fill="#8e8e93"/><rect x="10" y="1" width="12" height="6" rx="2" fill="#8e8e93"/><circle cx="16" cy="14" r="6" fill="#f7f7f8"/><circle cx="16" cy="14" r="4" fill="#8e8e93"/></svg>
      <div class="compose-field">Message</div>
      <svg class="icon-mic-round" width="36" height="36" viewBox="0 0 36 36"><circle cx="18" cy="18" r="18" fill="#8e8e93"/><rect x="14" y="8" width="8" height="14" rx="4" fill="#fff"/><path d="M11 18 Q11 25 18 25 Q25 25 25 18" fill="none" stroke="#fff" stroke-width="2"/><line x1="18" y1="25" x2="18" y2="29" stroke="#fff" stroke-width="2"/></svg>
    </div>

    <section class="keyboard">
      <div class="key-row">
        <span class="key">Q</span><span class="key">W</span><span class="key">E</span><span class="key">R</span><span class="key">T</span><span class="key">Y</span><span class="key">U</span><span class="key">I</span><span class="key">O</span><span class="key">P</span>
      </div>
      <div class="key-row row-two">
        <span class="key">A</span><span class="key">S</span><span class="key">D</span><span class="key">F</span><span class="key">G</span><span class="key">H</span><span class="key">J</span><span class="key">K</span><span class="key">L</span>
      </div>
      <div class="key-row row-three">
        <span class="key shift"><svg width="28" height="26" viewBox="0 0 28 26"><path d="M14 1 L27 14 L20 14 L20 25 L8 25 L8 14 L1 14 Z" fill="#111"/></svg></span>
        <span class="key">Z</span><span class="key">X</span><span class="key">C</span><span class="key">V</span><span class="key">B</span><span class="key">N</span><span class="key">M</span>
        <span class="key delete dark"><svg width="34" height="22" viewBox="0 0 34 22"><path d="M10 1 L32 1 Q33 1 33 3 L33 19 Q33 21 32 21 L10 21 L1 11 Z" fill="#fff"/><path d="M16 6 L26 16 M26 6 L16 16" stroke="#abb0ba" stroke-width="2"/></svg></span>
      </div>
      <div class="key-row row-bottom">
        <span class="key dark numbers">123</span>
        <span class="key dark globe"><svg width="30" height="30" viewBox="0 0 30 30" fill="none" stroke="#111" stroke-width="1.6"><circle cx="15" cy="15" r="13"/><ellipse cx="15" cy="15" rx="6" ry="13"/><line x1="2" y1="15" x2="28" y2="15"/><path d="M5 8 H25 M5 22 H25"/></svg></span>
        <span class="key dictate"><svg width="18" height="30" viewBox="0 0 18 30" fill="none" stroke="#111" stroke-width="1.6"><rect x="5" y="1" width="8" height="17" rx="4"/><path d="M2 14 Q2 23 9 23 Q16 23 16 14"/><line x1="9" y1="23" x2="9" y2="28"/><line x1="5" y1="28" x2="13" y2="28"/></svg></span>
        <span class="key space">space</span>
        <span class="key search">Search</span>
      </div>
    </section>
  </main>
</body>
</html>
```